Bright Willow Wellness
Heal your Body Mind and Spirit
Bright Willow Wellness - Health
Creative Brief
Professional
Melora T. Grant, MSW, LSW
Health Consultant and Spiritual Counselor
Certifications: Feeling Map Form Key Spiritual Counseling
melora@brightwillowwellness.example
www.brightwillowwellness.example
Next appointment: _____________________________________
guest guest
where is the logo
mgrant417 mgrant417
Designers: Please only design for business cards, not stationary. Thanks...

```html
<!DOCTYPE html>
<html lang="en">
<head>
<meta charset="utf-8">
<title>Bright Willow Wellness – Stationery</title>
<link rel="stylesheet" href="https://fonts.googleapis.com/css2?family=Cinzel:wght@600&family=Libre+Baskerville:ital,wght@1,700&family=Lato:wght@400;700&display=swap">
<style>
  :root{
    --bg:#e9ebee;
    --paper:#ffffff;
    --navy:#0d1f4f;
    --teal:#2a7c9c;
    --sky:#8dbad0;
    --mist:#d8e6ee;
    --ink:#1c2a4a;
    --grey:#7a8594;
  }
  *{box-sizing:border-box;margin:0;padding:0}
  html,body{width:1200px;height:936px;overflow:hidden;background:var(--bg)}
  body{position:relative;font-family:"Lato",sans-serif;color:var(--ink)}
  .sheet{position:absolute;background:var(--paper);overflow:hidden}
  .wave{position:absolute;left:0;bottom:0;width:100%;display:block}
  .w-light{fill:var(--mist)}
  .w-sky{fill:var(--sky)}
  .w-teal{fill:var(--teal)}
  .w-navy{fill:var(--navy)}
  .dot{display:inline-block;border-radius:50%;background:var(--teal);flex:none}
  .brand-name{font-family:"Cinzel",serif;font-weight:600;color:var(--navy);letter-spacing:.04em;white-space:nowrap}
  .tagline{font-family:"Libre Baskerville",serif;font-style:italic;font-weight:700;color:var(--navy);white-space:nowrap}
  .url{position:absolute;font-family:"Cinzel",serif;font-weight:600;color:#fff;letter-spacing:.28em;white-space:nowrap}

  /* Letterhead */
  .letterhead{left:182px;top:68px;width:388px;height:539px}
  .letterhead .brand{position:absolute;left:22px;top:20px;display:flex;align-items:center;gap:7px}
  .letterhead .brand .dot{width:18px;height:18px}
  .letterhead .brand-name{font-size:9px}
  .letterhead .tagline{font-size:5px}
  .letterhead .contact{position:absolute;left:250px;top:20px;font-size:5.5px;line-height:1.6;color:var(--grey)}
  .letterhead .faint-mark{position:absolute;left:162px;top:230px;width:160px;height:160px;border-radius:50%;background:var(--mist);opacity:.7}
  .letterhead .url{left:0;right:0;bottom:13px;text-align:center;font-size:7px}

  /* Presentation folder */
  .folder{left:633px;top:38px;width:493px;height:574px}
  .folder .dot{position:absolute;left:219px;top:172px;width:54px;height:54px}
  .folder .brand-name{position:absolute;left:0;right:0;top:240px;text-align:center;font-size:22px}
  .folder .tagline{position:absolute;left:0;right:0;top:272px;text-align:center;font-size:10px}
  .folder .url{left:0;right:0;bottom:28px;text-align:center;font-size:9px}

  /* Business cards */
  .card{width:220px;height:104px;border-radius:2px}
  .card-front{left:46px;top:651px}
  .card-front .brand{position:absolute;left:10px;top:10px;display:flex;align-items:center;gap:5px}
  .card-front .dot{width:12px;height:12px}
  .card-front .brand-name{font-size:7px}
  .card-front .details{position:absolute;left:10px;top:30px;font-size:5px;line-height:1.55;color:var(--grey)}
  .card-front .details strong{color:var(--navy);font-size:5.5px}
  .card-back{left:46px;top:767px}
  .card-back .appointment{position:absolute;left:12px;top:14px;font-size:5.5px;line-height:2.4;color:var(--grey)}
  .card-back .rule{display:inline-block;width:120px;border-bottom:.6px solid var(--grey);margin-left:4px;vertical-align:middle}

  /* Envelopes */
  .envelope-front{left:280px;top:658px;width:420px;height:192px}
  .envelope-front .brand{position:absolute;left:26px;top:16px;display:flex;align-items:center;gap:7px}
  .envelope-front .dot{width:16px;height:16px}
  .envelope-front .brand-name{font-size:9px}
  .envelope-front .tagline{font-size:5px}
  .envelope-back{left:738px;top:652px;width:426px;height:228px}
  .envelope-back .flap{position:absolute;left:0;top:0;width:100%;height:110px;display:block}
  .envelope-back .url{left:0;right:0;top:16px;text-align:center;font-size:8px;letter-spacing:.22em}
</style>
</head>
<body>

  <section class="sheet letterhead" aria-label="Letterhead">
    <div class="brand">
      <span class="dot"></span>
      <div>
        <div class="brand-name">Bright Willow Wellness</div>
        <div class="tagline">Achieve balanced health and well-being</div>
      </div>
    </div>
    <div class="contact">
      Melora T. Grant, MSW, LSW<br>
      Phone (555) 014-2287<br>
      melora@brightwillowwellness.example
    </div>
    <div class="faint-mark"></div>
    <svg class="wave" viewBox="0 0 400 100" height="92" preserveAspectRatio="none" aria-hidden="true">
      <path class="w-light" d="M0 34 C120 6 270 4 400 20 L400 100 L0 100Z"/>
      <path class="w-sky" d="M0 44 C130 16 270 12 400 28 L400 100 L0 100Z"/>
      <path class="w-teal" d="M0 52 C130 26 270 22 400 36 L400 100 L0 100Z"/>
      <path class="w-navy" d="M0 60 C130 36 270 30 400 44 L400 100 L0 100Z"/>
    </svg>
    <div class="url">www.brightwillowwellness.example</div>
  </section>

  <section class="sheet folder" aria-label="Presentation folder">
    <span class="dot"></span>
    <div class="brand-name">Bright Willow Wellness</div>
    <div class="tagline">Achieve balanced health and well-being</div>
    <svg class="wave" viewBox="0 0 400 100" height="110" preserveAspectRatio="none" aria-hidden="true">
      <path class="w-light" d="M0 30 C120 4 270 2 400 18 L400 100 L0 100Z"/>
      <path class="w-sky" d="M0 40 C130 14 270 10 400 26 L400 100 L0 100Z"/>
      <path class="w-teal" d="M0 48 C130 24 270 20 400 34 L400 100 L0 100Z"/>
      <path class="w-navy" d="M0 56 C130 34 270 28 400 42 L400 100 L0 100Z"/>
    </svg>
    <div class="url">www.brightwillowwellness.example</div>
  </section>

  <section class="sheet card card-front" aria-label="Business card front">
    <div class="brand">
      <span class="dot"></span>
      <span class="brand-name">Bright Willow Wellness</span>
    </div>
    <div class="details">
      <strong>Melora T. Grant, MSW, LSW</strong><br>
      Health Consultant and Spiritual Counselor<br>
      Phone (555) 014-2287<br>
      melora@brightwillowwellness.example
    </div>
    <svg class="wave" viewBox="0 0 400 100" height="26" preserveAspectRatio="none" aria-hidden="true">
      <path class="w-sky" d="M0 40 C130 14 270 10 400 26 L400 100 L0 100Z"/>
      <path class="w-navy" d="M0 56 C130 34 270 28 400 42 L400 100 L0 100Z"/>
    </svg>
  </section>

  <section class="sheet card card-back" aria-label="Business card back">
    <div class="appointment">
      Next appointment:<br>
      Date<span class="rule"></span><br>
      Time<span class="rule"></span>
    </div>
  </section>

  <section class="sheet envelope-front" aria-label="Envelope front">
    <div class="brand">
      <span class="dot"></span>
      <div>
        <div class="brand-name">Bright Willow Wellness</div>
        <div class="tagline">Achieve balanced health and well-being</div>
      </div>
    </div>
  </section>

  <section class="sheet envelope-back" aria-label="Envelope back">
    <svg class="flap" viewBox="0 0 426 110" preserveAspectRatio="none" aria-hidden="true">
      <path class="w-navy" d="M0 0 H426 V40 L226 108 Q213 112 200 108 L0 40Z"/>
    </svg>
    <div class="url">www.brightwillowwellness.example</div>
  </section>

</body>
</html>
```